Law firm website marketed direct to many individual clients

I need someone to design a very basic website for a law firm that will be very eye catching. It's going to be a single-paged, scrolling website with a small number of folds. I have uploaded a simple word document that outlines the basics of what I thought could be the layout, but I am open to suggestion on font, size, shades of color, organization, etc. etc. Essentially the website just needs to be a very efficient and visually appealing way of conveying some simple messages.

Target Market(s)

High volumes of individuals who have gotten into a car accident and then google on their phones a lawyer to hire to represent them.

Industry/Entity Type

Legal

Number of Pages Required

1 page

Font styles to use
Serif
Sans Serif

Colors
34a7d7
85cae6
0592cd

Requirements
Must have
• Must be bright and grab the users attention with color scheme and layout. The different sections should be done in such a way that they can fit entirely onto one smart phone or tablet screen.
Nice to have
• I'd like to try and see what it looks like if in the middle somewhere there is a fold that says "MEET YOUR ATTORNEYS" and includes individual photos of two attorneys, one on the left side and one on the right. And then a small bio section on them. I don't want the photos to include a square or rectangle background, I want the person in the photo to be superimposed on top of whatever pattern or background you have in the fold.
Should not have
• Do not want too much text. Anything more than 2 sentences in any single place is unacceptable.

```html
<!DOCTYPE html>
<html lang="en">
<head>
<meta charset="utf-8">
<title>Harborline Law Group</title>
<link rel="stylesheet" href="https://fonts.googleapis.com/css2?family=Oswald:wght@300;400;700&family=Raleway:ital,wght@0,400;1,400&display=swap">
<style>
:root{
  --blue:#0a8ccb;
  --blue-deep:#0693cf;
  --blue-dark:#0a5f8e;
  --blue-soft:#5bb8e3;
  --paper:#f7f7f7;
  --fold-gray:#d3d4d6;
  --panel-gray:#dfe0e2;
  --form-gray:#8f8f8f;
  --ink:#2b2b2b;
  --ink-soft:#444;
  --white:#fff;
}
*{margin:0;padding:0;box-sizing:border-box}
html,body{width:1200px;height:2539px;overflow:hidden}
body{position:relative;background:var(--paper);font-family:'Oswald',sans-serif;color:var(--ink)}
.abs{position:absolute}

.topbar{left:0;top:0;width:1200px;height:69px;background:var(--paper)}
.topbar .brand{left:98px;top:22px;font-family:'Raleway',sans-serif;font-style:italic;font-size:24px;color:var(--ink)}
.topbar .phone{right:100px;top:22px;font-family:'Raleway',sans-serif;font-style:italic;font-size:23px;color:var(--ink)}

.hero{left:0;top:69px;width:1200px;height:826px;overflow:hidden}
.hero-photo{left:0;top:0;width:1200px;height:826px;background:linear-gradient(135deg,#2f8fc2 0%,#1a6fa3 45%,#0d4f7e 100%)}
.hero-shapes{left:0;top:0}
.headline{right:464px;top:228px;text-align:right;color:var(--white);font-weight:400;font-size:98px;line-height:100px}
.tagline{left:315px;top:444px;width:379px;height:47px;background:var(--blue);color:var(--white);font-weight:300;font-size:29px;line-height:47px;text-align:center}
.form-label{left:795px;font-family:'Raleway',sans-serif;font-size:26px;color:var(--ink)}
.field{background:var(--white);border:1px solid #cfcfcf;border-radius:3px;height:33px}
.cta{left:789px;top:603px;width:411px;height:51px;background:var(--blue-dark);border-radius:12px 0 0 12px;color:var(--white);font-size:20px;letter-spacing:2px;line-height:51px;text-align:center;font-weight:400}
.contact-label{right:96px;top:742px;color:var(--white);font-size:24px;letter-spacing:2px}
.contact-phone{right:96px;top:768px;color:var(--white);font-weight:300;font-size:41px;letter-spacing:5px}

.learn{left:0;width:1200px;top:910px;text-align:center;font-weight:300;font-size:26px;color:var(--ink)}
.chevrons{left:582px;top:958px}

.feature-icon{top:1103px}
.feature-title{color:var(--blue);font-weight:300;font-size:22px;line-height:25px;text-transform:uppercase}
.feature-text{top:1206px;font-weight:300;font-size:20px;line-height:27px;color:var(--ink)}

.call-word{left:403px;top:1380px;font-weight:700;font-size:54px;letter-spacing:5px;line-height:70px;color:var(--ink)}
.btn{background:var(--blue);color:var(--white);font-weight:400;font-size:22px;letter-spacing:3px;text-align:center}
.call-btn{left:521px;top:1388px;width:251px;height:54px;line-height:54px}

.fold{left:0;top:1467px;width:1200px;height:468px;background:var(--fold-gray);overflow:hidden}
.fold-shape{left:0;top:0}
.promise{right:455px;top:62px;text-align:right;font-size:128px;line-height:137px;font-weight:300;color:var(--white)}
.promise .accent{color:var(--blue);font-weight:400}
.quote{left:840px;top:123px;width:258px;text-align:right;color:var(--white);font-weight:700;font-size:22px;line-height:36.5px;letter-spacing:4px}

.questions-title{left:0;width:1240px;top:1966px;text-align:center;color:var(--blue);font-size:32px;letter-spacing:6px;font-weight:400}
.questions-text{left:258px;width:716px;top:2022px;text-align:center;color:var(--ink-soft);font-weight:300;font-size:23px;line-height:36px;letter-spacing:2.5px}
.questions-text .link{color:var(--blue)}
.questions-btn{left:493px;top:2180px;width:250px;height:52px;line-height:52px}

.footer{left:0;top:2261px;width:1200px;height:278px;background:var(--blue-deep)}
.footer .divider{left:605px;top:29px;width:2px;height:240px;background:#1f5f85}
.footer .name{left:162px;top:108px;color:var(--white);font-weight:300;font-size:37px;letter-spacing:3px}
.footer .info{left:770px;color:var(--white);font-size:22px;letter-spacing:2.5px;font-weight:400;line-height:34px}
.footer .rule{left:770px;top:159px;width:205px;height:2px;background:#1f5f85}
.footer .icon{left:722px}
</style>
</head>
<body>

<header class="topbar abs">
  <div class="brand abs">Harborline Law Group</div>
  <div class="phone abs">504-555-0182</div>
</header>

<section class="hero abs">
  <div class="hero-photo abs" role="img" aria-label="Blue-toned photo of a judge's gavel, law books and scales of justice on a wooden desk"></div>
  <svg class="hero-shapes abs" width="1200" height="826" viewBox="0 0 1200 826">
    <polygon points="914,0 1200,0 1200,740 609,740" fill="var(--panel-gray)"/>
    <polygon points="738,427 1200,427 1200,667 640,667" fill="var(--form-gray)"/>
  </svg>
  <h1 class="headline abs">YOUR CASE<br>YOUR MONEY</h1>
  <div class="tagline abs">ACCIDENT? INJURED?</div>

  <div class="form-label abs" style="top:448px">Name</div>
  <div class="form-label abs" style="top:492px">Phone#</div>
  <div class="form-label abs" style="top:543px">Email</div>
  <div class="field abs" style="left:902px;top:440px;width:97px"></div>
  <div class="field abs" style="left:1010px;top:440px;width:160px"></div>
  <div class="field abs" style="left:902px;top:488px;width:268px"></div>
  <div class="field abs" style="left:902px;top:539px;width:268px"></div>
  <div class="cta abs">FIND OUT WHAT YOUR CASE IS WORTH</div>

  <div class="contact-label abs">Contact Us</div>
  <div class="contact-phone abs">504-555-0182</div>
</section>

<div class="learn abs">Learn More</div>
<svg class="chevrons abs" width="36" height="34" viewBox="0 0 36 34">
  <polyline points="3,3 18,15 33,3" fill="none" stroke="var(--blue-soft)" stroke-width="6"/>
  <polyline points="3,17 18,29 33,17" fill="none" stroke="var(--blue-soft)" stroke-width="6"/>
</svg>

<!-- Features -->
<svg class="feature-icon abs" style="left:98px" width="34" height="48" viewBox="0 0 34 48">
  <path d="M6 10 L17 2 L28 10 V46 H6 Z" fill="var(--blue)"/>
  <circle cx="17" cy="10" r="3" fill="var(--paper)"/>
  <text x="17" y="36" text-anchor="middle" font-family="Oswald,sans-serif" font-size="15" fill="#fff">%</text>
</svg>
<div class="feature-title abs" style="left:137px;top:1123px">Low Fees</div>
<div class="feature-text abs" style="left:142px;width:90px">We charge less, so you keep more.</div>

<svg class="feature-icon abs" style="left:320px" width="56" height="46" viewBox="0 0 56 46">
  <path d="M4 22 C4 10 16 4 28 4 C42 4 54 11 54 22 C54 33 42 39 28 39 C24 39 20 38 17 37 L6 43 L10 33 C6 30 4 26 4 22Z" fill="var(--blue)"/>
  <circle cx="19" cy="22" r="3.5" fill="#fff"/><circle cx="29" cy="22" r="3.5" fill="#fff"/><circle cx="39" cy="22" r="3.5" fill="#fff"/>
</svg>
<div class="feature-title abs" style="left:383px;top:1120px">Free Consultation</div>
<div class="feature-text abs" style="left:388px;width:150px">It's always free to talk to us.</div>

<svg class="feature-icon abs" style="left:633px" width="50" height="50" viewBox="0 0 50 50">
  <path d="M10 4 L18 4 L22 15 L16 20 C19 27 23 31 30 34 L35 28 L46 32 L46 40 C46 44 42 47 38 46 C20 42 8 30 4 12 C3 8 6 4 10 4Z" fill="var(--blue)"/>
  <path d="M28 6 A16 16 0 0 1 44 22" fill="none" stroke="var(--blue)" stroke-width="4"/>
  <path d="M28 14 A8 8 0 0 1 36 22" fill="none" stroke="var(--blue)" stroke-width="4"/>
</svg>
<div class="feature-title abs" style="left:699px;top:1099px">Get Started Using<br>Only Your Phone</div>
<div class="feature-text abs" style="left:690px;width:165px">No need to come to the office, sign up using your phone.</div>

<svg class="feature-icon abs" style="left:912px" width="46" height="46" viewBox="0 0 46 46">
  <circle cx="11" cy="7" r="5" fill="var(--blue)"/><circle cx="23" cy="7" r="5" fill="var(--blue)"/><circle cx="35" cy="7" r="5" fill="var(--blue)"/>
  <rect x="2" y="15" width="9" height="20" fill="var(--blue)"/>
  <rect x="35" y="15" width="9" height="20" fill="var(--blue)"/>
  <rect x="14" y="21" width="18" height="5" fill="var(--blue)"/>
  <rect x="20" y="26" width="6" height="18" fill="var(--blue)"/>
  <rect x="4" y="35" width="5" height="10" fill="var(--blue)"/><rect x="37" y="35" width="5" height="10" fill="var(--blue)"/>
</svg>
<div class="feature-title abs" style="left:970px;top:1099px">Speak Directly<br>To A Lawyer</div>
<div class="feature-text abs" style="left:970px;width:130px">No staff screening. Talk</div>

<div class="call-word abs">Call</div>
<div class="btn call-btn abs">504-555-0182</div>

<section class="fold abs">
  <svg class="fold-shape abs" width="1200" height="468" viewBox="0 0 1200 468">
    <polygon points="870,0 1200,0 1200,468 718,468" fill="var(--blue-deep)"/>
  </svg>
  <h2 class="promise abs">NO FEE <span class="accent">UNLESS</span><br>WE <span class="accent">WIN</span></h2>
  <p class="quote abs">“We don't get paid unless you get paid. It's as simple as that. We let our results do the talking for us.”</p>
</section>

<h2 class="questions-title abs">QUESTIONS ABOUT ANYTHING?</h2>
<p class="questions-text abs">We're here to help. Feel free to call us at <span class="link">504-555-0182</span> to speak to one of our attorneys. With extensive experience in helping clients get the results that they want, our team is always just a phone call away.</p>
<div class="btn questions-btn abs">504-555-0182</div>

<footer class="footer abs">
  <div class="divider abs"></div>
  <div class="name abs">Harborline Law Group</div>
  <svg class="icon abs" style="top:90px" width="18" height="22" viewBox="0 0 18 22">
    <path d="M9 1 C4 1 2 5 2 8 C2 13 9 19 9 19 C9 19 16 13 16 8 C16 5 14 1 9 1Z" fill="#1b1b1b"/>
    <circle cx="9" cy="8" r="3" fill="var(--blue-deep)"/>
    <rect x="1" y="19" width="16" height="2" fill="#1b1b1b"/>
  </svg>
  <div class="info abs" style="top:86px">Riverside Office Suite<br>Lakeview, LA 70999</div>
  <div class="rule abs"></div>
  <svg class="icon abs" style="top:178px" width="18" height="16" viewBox="0 0 18 16">
    <path d="M2 5 C2 2 5 1 9 1 C13 1 16 2 16 5 L13 6 L12 4 H6 L5 6Z" fill="#1b1b1b"/>
    <rect x="4" y="8" width="10" height="7" rx="1" fill="#1b1b1b"/>
  </svg>
  <div class="info abs" style="top:169px">504-555-0182</div>
</footer>

</body>
</html>
```